Blueprints For A Steady Home Book*

Our book is about using engineering and biblical principles to solve problems in marriage. We are the wedlock Architects. See our branded logo in the attachments. We would like to see different types of graphics that shows continuous improvement in marriage. Our colors should be Gold Black and Red. Could use white text and symbols if needed. Brief description on the back with some quotes and our Picture. Use 5.5x8.5 as the size of the book. Not sure about the spine size.

Target Market(s)

Married couples

Font styles to use
Serif

Colors

Designer to choose colors to be used in the design.

Requirements
Nice to have
• Engineering symbols and Logos.

```html
<!DOCTYPE html>
<html lang="en">
<head>
<meta charset="utf-8">
<title>Blueprints For A Steady Home — Front Cover</title>
<link rel="stylesheet" href="https://fonts.googleapis.com/css2?family=Cinzel:wght@400;500;600&display=swap">
<style>
  :root {
    --paper: #ffffff;
    --title-red: #8e1b1e;
    --title-red-light: #b3262a;
    --gold-deep: #b86a18;
    --gold-mid: #d98f32;
    --gold-light: #e8ad55;
    --ink: #111111;
    --art-gold: #d9a437;
    --art-glow: #f3d27c;
    --art-pale: #f7ecd2;
  }
  html, body {
    margin: 0;
    padding: 0;
    width: 777px;
    height: 1200px;
    overflow: hidden;
    background: var(--paper);
  }
  .cover {
    position: relative;
    width: 777px;
    height: 1200px;
    background: var(--paper);
    overflow: hidden;
    font-family: "Cinzel", "Times New Roman", serif;
  }
  .cover-illustration {
    position: absolute;
    left: 232px;
    top: 24px;
    width: 400px;
    height: 470px;
    border-radius: 18px;
    background: linear-gradient(180deg, var(--art-pale) 0%, var(--art-glow) 55%, var(--art-gold) 100%);
  }
  .title {
    position: absolute;
    left: 0;
    right: 0;
    top: 548px;
    margin: 0;
    text-align: center;
    color: var(--title-red);
    font-weight: 600;
    line-height: 1;
  }
  .title span { display: block; }
  .title-lead {
    font-size: 60px;
    letter-spacing: 1px;
  }
  .title-main {
    font-size: 150px;
    margin-top: 18px;
    background: linear-gradient(180deg, var(--title-red-light), var(--title-red));
    -webkit-background-clip: text;
    background-clip: text;
    color: transparent;
  }
  .title-main + .title-main { margin-top: 6px; }
  .author-band {
    position: absolute;
    left: 0;
    bottom: 0;
    width: 777px;
    height: 175px;
    background: linear-gradient(180deg, var(--gold-deep) 0%, var(--gold-mid) 45%, var(--gold-light) 100%);
    display: flex;
    align-items: center;
    justify-content: center;
  }
  .author-name {
    margin: 0;
    color: var(--ink);
    font-size: 66px;
    font-weight: 500;
    letter-spacing: 1px;
  }
</style>
</head>
<body>
  <main class="cover">
    <div class="cover-illustration" role="img" aria-label="Illustration: a crane hook lifting two interlocked gold wedding rings and a yellow hard hat"></div>

    <h1 class="title">
      <span class="title-lead">Blueprints for a</span>
      <span class="title-main">Steady</span>
      <span class="title-main">Home</span>
    </h1>

    <footer class="author-band">
      <p class="author-name">Author Name</p>
    </footer>
  </main>
</body>
</html>
```